Wireless internet service provider needs flyer to lease property to build new tower sites

We need a flyer to leave behind at customer sites that we would like to turn into a tower location. We want to lease roof space or property from the customer to expand our network. We would like it to read as a sales ad that they can make up to $200/mo in exchange for signing a lease agreement with us. Attached are example photos of what typical residential tower sites look like. Contact number 530-555-0147 and email sales@brightwavelink.net. This will be left behind at a customer site, after a technician visits. It will be used as sales/marketing material. The flyer should be a 6x11 postcard.
Text to add to the flyer are the following points.
- Earn passive income
- Help your community get better internet
- We pay for all build costs

Target Market(s)

Rural residences

Industry/Entity Type

Internet Services

Requirements
Must have
• Sales pitch of "get paid up to $300/mo to host wireless equipment for our local rural ISP"

```html
<!DOCTYPE html>
<html lang="en">
<head>
<meta charset="utf-8">
<title>Tower Site Lease Postcard</title>
<link rel="stylesheet" href="https://fonts.googleapis.com/css2?family=Krona+One&family=Michroma&family=Poppins:wght@400;500;600;700;800&display=swap">
<style>
  :root {
    --ink: #0d0d0d;
    --red: #b01e35;
    --red-deep: #8e1428;
    --paper: #eeeced;
    --footer: #e5e2e3;
    --text-dark: #1f1f1f;
    --text-body: #333333;
    --page: #f4f4f4;
  }
  html, body {
    margin: 0;
    padding: 0;
    width: 800px;
    height: 1200px;
    overflow: hidden;
    background: var(--page);
  }
  .postcard {
    position: absolute;
    left: 20px;
    top: 328px;
    width: 760px;
    height: 543px;
    box-shadow: 0 8px 22px rgba(0,0,0,0.22);
  }
  .postcard svg { display: block; }
  .display { font-family: "Krona One", "Michroma", sans-serif; }
  .wide-light { font-family: "Michroma", sans-serif; }
  .sans { font-family: "Poppins", sans-serif; }
</style>
</head>
<body>
<div class="postcard">
  <svg width="760" height="543" viewBox="0 0 760 543" xmlns="http://www.w3.org/2000/svg">
    <defs>
      <linearGradient id="screenTone" x1="0" y1="0" x2="0" y2="1">
        <stop offset="0" stop-color="#8a8a8a"/>
        <stop offset="0.5" stop-color="#3c3c3c"/>
        <stop offset="1" stop-color="#1b1a14"/>
      </linearGradient>
      <linearGradient id="coinTone" x1="0" y1="0" x2="1" y2="0">
        <stop offset="0" stop-color="#4a2a12"/>
        <stop offset="0.5" stop-color="#b06a2c"/>
        <stop offset="1" stop-color="#3a1f0c"/>
      </linearGradient>
      <linearGradient id="bandTone" x1="0" y1="0" x2="1" y2="0">
        <stop offset="0" stop-color="#9c1a2e"/>
        <stop offset="1" stop-color="#b01e35"/>
      </linearGradient>
    </defs>

    <!-- card base -->
    <rect class="card-paper" x="0" y="0" width="760" height="543" fill="var(--paper)"/>

    <!-- header band -->
    <path class="header-band" d="M0 0 H760 V148 H410 C372 148 362 122 318 122 H0 Z" fill="var(--ink)"/>
    <path class="header-rule" d="M0 122 H318 C362 122 372 148 410 148 H760" fill="none" stroke="var(--red)" stroke-width="3"/>
    <path class="header-swoosh" d="M300 122 C350 121 362 146 410 149 L380 149 C352 140 340 124 300 124 Z" fill="var(--red)"/>

    <text class="display headline-get" x="46" y="66" font-size="34" fill="#ffffff" textLength="113" lengthAdjust="spacingAndGlyphs">GET</text>
    <text class="display headline-paid" x="46" y="102" font-size="34" fill="#ffffff" textLength="130" lengthAdjust="spacingAndGlyphs">PAID</text>
    <text class="wide-light headline-upto" x="203" y="50" font-size="21" fill="#ffffff" textLength="92" lengthAdjust="spacingAndGlyphs">UP TO</text>
    <text class="display headline-amount" x="203" y="102" font-size="46" fill="var(--red)" textLength="518" lengthAdjust="spacingAndGlyphs">$300/MONTH</text>

    <!-- monitor image area -->
    <rect class="monitor-image" x="18" y="137" width="330" height="320" rx="6" fill="url(#screenTone)" role="img" aria-label="Desktop monitor showing a city skyline at night with network lines"/>

    <!-- coins image area and rising arrow -->
    <rect class="coins-image" x="636" y="150" width="120" height="64" rx="8" fill="url(#coinTone)" role="img" aria-label="Stacks of copper coins"/>
    <path class="rise-arrow" d="M622 163 C664 158 694 144 712 122" fill="none" stroke="var(--red)" stroke-width="3"/>
    <path class="rise-arrowhead" d="M718 113 L704 119 L714 127 Z" fill="var(--red)"/>

    <!-- lease headline -->
    <text class="sans lease-line1" x="367" y="191" font-size="32" font-weight="800" fill="var(--ink)" textLength="248" lengthAdjust="spacingAndGlyphs">IN EXCHANGE</text>
    <text class="sans lease-line2" x="367" y="215" font-size="24" font-weight="500" fill="var(--ink)" textLength="201" lengthAdjust="spacingAndGlyphs">FOR SIGNING A</text>
    <text class="sans lease-line3" x="367" y="245" font-size="33" font-weight="800" fill="var(--red)" textLength="336" lengthAdjust="spacingAndGlyphs">LEASE AGREEMENT</text>
    <text class="sans lease-line4" x="368" y="266" font-size="21" font-weight="800" fill="var(--red)" textLength="125" lengthAdjust="spacingAndGlyphs">WITH US...</text>

    <!-- feature band -->
    <rect class="feature-band" x="343" y="276" width="417" height="50" fill="url(#bandTone)"/>
    <g class="feature feature-contracts">
      <circle cx="380" cy="301" r="13" fill="#ffffff"/>
      <rect x="374" y="293" width="12" height="16" rx="1.5" fill="none" stroke="var(--text-dark)" stroke-width="1.6"/>
      <path d="M377 298 H383 M377 301 H383 M377 304 H381" stroke="var(--text-dark)" stroke-width="1.2"/>
      <text class="sans" x="401" y="296" font-size="12" font-weight="700" fill="#ffffff">NO</text>
      <text class="sans" x="401" y="310" font-size="12" font-weight="700" fill="#ffffff">CONTRACTS</text>
    </g>
    <g class="feature feature-install">
      <circle cx="510" cy="301" r="13" fill="#ffffff"/>
      <circle cx="510" cy="301" r="6" fill="none" stroke="var(--text-dark)" stroke-width="3" stroke-dasharray="2.4 1.6"/>
      <circle cx="510" cy="301" r="2" fill="var(--text-dark)"/>
      <text class="sans" x="527" y="296" font-size="12" font-weight="700" fill="#ffffff">FREE</text>
      <text class="sans" x="527" y="310" font-size="12" font-weight="700" fill="#ffffff">INSTLLATION</text>
    </g>
    <g class="feature feature-data">
      <circle cx="639" cy="301" r="13" fill="#ffffff"/>
      <rect x="631" y="296" width="16" height="11" rx="2" fill="none" stroke="var(--text-dark)" stroke-width="1.5"/>
      <path d="M635 301.5 C635 298.5 639 298.5 639 301.5 C639 304.5 643 304.5 643 301.5 C643 298.5 639 298.5 639 301.5 C639 304.5 635 304.5 635 301.5 Z" fill="none" stroke="var(--text-dark)" stroke-width="1"/>
      <path d="M634 296 V292 M639 296 V290 M644 296 V292" stroke="var(--text-dark)" stroke-width="1.3"/>
      <text class="sans" x="656" y="296" font-size="12" font-weight="700" fill="#ffffff">UNLIMITED</text>
      <text class="sans" x="656" y="310" font-size="12" font-weight="700" fill="#ffffff">DATA</text>
    </g>

    <!-- detail points -->
    <g class="detail-point detail-pitch">
      <circle cx="390" cy="340" r="4.5" fill="none" stroke="var(--red)" stroke-width="1.3"/>
      <path d="M387.5 340 L389.5 342.5 L394 336" fill="none" stroke="var(--text-dark)" stroke-width="1.4"/>
      <text class="sans" font-size="9.5" font-weight="600" fill="var(--red)">
        <tspan x="400" y="343">Get paid up to $300/mo to host wireless equipment</tspan>
        <tspan x="400" y="354">for our local rural ISP.</tspan>
      </text>
    </g>
    <g class="detail-point detail-income">
      <circle cx="390" cy="364" r="4.5" fill="none" stroke="var(--red)" stroke-width="1.3"/>
      <path d="M387.5 364 L389.5 366.5 L394 360" fill="none" stroke="var(--text-dark)" stroke-width="1.4"/>
      <text class="sans" x="400" y="367" font-size="9.5" fill="var(--text-body)">Earn passive income</text>
    </g>
    <g class="detail-point detail-costs">
      <circle cx="550" cy="364" r="4.5" fill="none" stroke="var(--red)" stroke-width="1.3"/>
      <path d="M547.5 364 L549.5 366.5 L554 360" fill="none" stroke="var(--text-dark)" stroke-width="1.4"/>
      <text class="sans" x="560" y="367" font-size="9.5" fill="var(--text-body)">We pay for all build costs</text>
    </g>
    <g class="detail-point detail-community">
      <circle cx="390" cy="377" r="4.5" fill="none" stroke="var(--red)" stroke-width="1.3"/>
      <path d="M387.5 377 L389.5 379.5 L394 373" fill="none" stroke="var(--text-dark)" stroke-width="1.4"/>
      <text class="sans" x="400" y="380" font-size="9.5" fill="var(--text-body)">Help your community get better internet</text>
    </g>
    <line class="detail-divider" x1="387" y1="387" x2="745" y2="387" stroke="#b9b6b7" stroke-width="0.8"/>
    <g class="detail-point">
      <circle cx="390" cy="396" r="4.5" fill="none" stroke="var(--red)" stroke-width="1.3"/>
      <path d="M387.5 396 L389.5 398.5 L394 392" fill="none" stroke="var(--text-dark)" stroke-width="1.4"/>
      <text class="sans" x="400" y="399" font-size="9.5" fill="var(--text-body)" textLength="345" lengthAdjust="spacingAndGlyphs">Our equipment is very low power typically under 250mw and directional.</text>
    </g>
    <g class="detail-point">
      <circle cx="390" cy="409" r="4.5" fill="none" stroke="var(--red)" stroke-width="1.3"/>
      <path d="M387.5 409 L389.5 411.5 L394 405" fill="none" stroke="var(--text-dark)" stroke-width="1.4"/>
      <text class="sans" font-size="9.5" fill="var(--text-body)">
        <tspan x="400" y="412">We take into consideration the look of the equipment and</tspan>
        <tspan x="400" y="423">mounting to either hide or at least make the antennas look</tspan>
        <tspan x="400" y="434">high-tech and appealing.</tspan>
      </text>
    </g>

    <!-- footer -->
    <path class="footer-panel" d="M0 467 H330 C362 467 366 443 400 443 H760 V543 H0 Z" fill="var(--footer)"/>
    <path class="footer-rule" d="M0 467 H330 C362 467 366 443 400 443 H760" fill="none" stroke="var(--red)" stroke-width="2.5"/>
    <path class="footer-swoosh" d="M318 467 C352 466 358 444 398 442 L380 442 C352 448 346 464 318 465 Z" fill="var(--red)"/>

    <g class="brand-name">
      <circle cx="48" cy="496" r="14" fill="var(--red)"/>
      <text class="sans" x="70" y="503" font-size="20" font-weight="800" fill="var(--text-dark)" textLength="222" lengthAdjust="spacingAndGlyphs">BrightWaveLink.net</text>
    </g>

    <line class="footer-divider" x1="320" y1="475" x2="320" y2="515" stroke="var(--text-dark)" stroke-width="1.2"/>
    <text class="display call-us" x="337" y="492" font-size="12.5" fill="var(--red)" textLength="86" lengthAdjust="spacingAndGlyphs">CALL US</text>
    <text class="wide-light call-today" x="429" y="492" font-size="15" fill="var(--text-dark)" textLength="107" lengthAdjust="spacingAndGlyphs">TODAY!</text>
    <path class="phone-icon" d="M344 503 C341 506 341 511 344 514 L345.5 512.5 C344 510 344 507 345.5 505 Z" fill="var(--red)"/>
    <text class="sans phone-number" x="350" y="513" font-size="16" font-weight="700" fill="var(--text-dark)" textLength="125" lengthAdjust="spacingAndGlyphs">530-555-0147</text>

    <line class="footer-divider" x1="553" y1="475" x2="553" y2="515" stroke="var(--text-dark)" stroke-width="1.2"/>
    <g class="email-icon">
      <rect x="566" y="477" width="13" height="9" rx="1" fill="var(--red)"/>
      <path d="M566 477 L572.5 482 L579 477" fill="none" stroke="#ffffff" stroke-width="1"/>
    </g>
    <text class="sans email" x="584" y="486" font-size="11.5" font-weight="700" fill="var(--text-dark)" textLength="162" lengthAdjust="spacingAndGlyphs">sales@brightwavelink.net</text>
    <g class="web-icon">
      <circle cx="572.5" cy="507" r="6" fill="none" stroke="var(--red)" stroke-width="1.4"/>
      <ellipse cx="572.5" cy="507" rx="2.5" ry="6" fill="none" stroke="var(--red)" stroke-width="1"/>
      <path d="M566.5 507 H578.5" stroke="var(--red)" stroke-width="1"/>
    </g>
    <text class="sans website" x="584" y="511" font-size="11.5" font-weight="700" fill="var(--text-dark)" textLength="150" lengthAdjust="spacingAndGlyphs">www.<tspan fill="var(--red)">brightwavelink</tspan>.net</text>
  </svg>
</div>
</body>
</html>
```